Hop Grower Producer Card

A wisconsin based grower of high quality mid westrn grown Hops with the concept of growing and processing Hops into pellet form for sale to brewers of beer large and small .varieties are grown are Cascade ,Chinook and Centennial

Target Market(s)

Brew masters at micro brews and large breweries

Industry/Entity Type

Processing

Font styles to use
Decorative
Script

Requirements
Must have
• i would like the Hop varieties listed on the back of the card , with the statement Grower of High Quality Wisconsin Hops and the web site address
Nice to have
• german style font for the name Velmar's Bine Hollow

```html
<!DOCTYPE html>
<html lang="en">
<head>
<meta charset="utf-8">
<title>Velmar's Bine Hollow – Business Cards</title>
<link href="https://fonts.googleapis.com/css2?family=UnifrakturMaguntia&family=Roboto+Condensed:wght@400;700&family=Roboto+Slab:wght@800&family=Montserrat:wght@500&display=swap" rel="stylesheet">
<style>
  :root{
    --page:#e9e9e9;
    --maroon:#5c0a06;
    --red:#d9141a;
    --yellow:#f5e21c;
    --white:#ffffff;
    --ink:#3a0503;
  }
  *{margin:0;padding:0;box-sizing:border-box}
  html,body{width:1200px;height:973px;overflow:hidden;background:var(--page)}
  .sheet{position:relative;width:1200px;height:973px}
  .card{position:absolute;width:760px;height:434px;left:220px;overflow:hidden;
        box-shadow:0 6px 18px rgba(0,0,0,.18);background:var(--maroon)}
  .card--back{top:38px}
  .card--front{top:502px}
  .card svg.shape{position:absolute;inset:0}
  .brand{font-family:"UnifrakturMaguntia",serif;color:var(--white);font-weight:400;white-space:nowrap}
  .tagline{font-family:"Roboto Condensed",sans-serif;font-weight:700;color:var(--yellow);
           text-transform:uppercase;white-space:nowrap}

  /* back */
  .back-brand{position:absolute;left:40px;top:112px;font-size:50px;transform:rotate(-6deg);transform-origin:left bottom}
  .back-tagline{position:absolute;left:44px;top:172px;font-size:19px;transform:rotate(-6deg);transform-origin:left bottom}
  .variety-band{position:absolute;left:-20px;top:218px;width:560px;height:58px;background:var(--red);
                transform:rotate(-6deg);transform-origin:left top;display:flex;align-items:center;padding-left:64px}
  .variety-band span{font-family:"Roboto Slab",serif;font-weight:800;font-size:27px;color:var(--yellow);white-space:nowrap}
  .web-pill{position:absolute;left:262px;top:282px;height:30px;padding:0 16px 0 8px;border-radius:15px;
            background:var(--yellow);display:flex;align-items:center;gap:7px;transform:rotate(-6deg);
            font-family:"Roboto Condensed",sans-serif;font-weight:700;font-size:16px;color:var(--ink)}

  /* front */
  .person{position:absolute;right:40px;top:30px;text-align:right;color:var(--white);font-family:"Montserrat",sans-serif}
  .person-name{font-size:20px;letter-spacing:3px;text-transform:uppercase}
  .person-role{font-size:14px;letter-spacing:2px;font-variant:small-caps}
  .front-brand{position:absolute;right:40px;top:92px;font-size:48px}
  .front-tagline{position:absolute;right:40px;top:150px;font-size:18px}
  .contacts{position:absolute;right:40px;top:196px;list-style:none;text-align:right;
            font-family:"Roboto Condensed",sans-serif;font-size:17px;color:var(--white)}
  .contacts li{display:flex;justify-content:flex-end;align-items:center;gap:6px;margin-bottom:9px;white-space:nowrap}
  .contacts .pair{gap:16px}
  .contacts .item{display:flex;align-items:center;gap:6px}
  .icon{width:16px;height:16px;flex:none}
</style>
</head>
<body>
<div class="sheet">

  <!-- Back of card: varieties -->
  <section class="card card--back">
    <svg class="shape" width="760" height="434" viewBox="0 0 760 434">
      <defs>
        <linearGradient id="beerScene" x1="0" y1="0" x2="1" y2="1">
          <stop offset="0" stop-color="#8a5a2e"/>
          <stop offset=".45" stop-color="#e2a53a"/>
          <stop offset=".75" stop-color="#c99a5a"/>
          <stop offset="1" stop-color="#6f9a3a"/>
        </linearGradient>
      </defs>
      <rect x="330" y="0" width="430" height="300" fill="url(#beerScene)" role="img" aria-label="Photo of a glass of beer with barrels, wheat and hop cones"/>
      <path d="M0 0 L390 0 Q430 210 760 300 L760 434 L0 434 Z" fill="var(--maroon)"/>
    </svg>
    <div class="brand back-brand">Velmar's Bine Hollow</div>
    <div class="tagline back-tagline">Grower of High Quality Wisconsin Hops</div>
    <div class="variety-band"><span>Cascade, Chinook, Centennial</span></div>
    <div class="web-pill">
      <svg class="icon" viewBox="0 0 16 16"><circle cx="8" cy="8" r="7" fill="none" stroke="var(--ink)" stroke-width="1.4"/><ellipse cx="8" cy="8" rx="3" ry="7" fill="none" stroke="var(--ink)" stroke-width="1.2"/><line x1="1" y1="8" x2="15" y2="8" stroke="var(--ink)" stroke-width="1.2"/></svg>
      www.binehollow.com
    </div>
  </section>

  <!-- Front of card: contact -->
  <section class="card card--front">
    <svg class="shape" width="760" height="434" viewBox="0 0 760 434">
      <defs>
        <linearGradient id="hopScene" x1="0" y1="0" x2="1" y2="1">
          <stop offset="0" stop-color="#7fb33a"/>
          <stop offset=".5" stop-color="#a9d35a"/>
          <stop offset="1" stop-color="#eef5e0"/>
        </linearGradient>
      </defs>
      <rect x="0" y="0" width="560" height="434" fill="url(#hopScene)" role="img" aria-label="Photo of fresh green hop cones and a hop leaf"/>
      <path d="M300 0 L760 0 L760 434 L560 434 Q330 300 300 0 Z" fill="var(--maroon)"/>
    </svg>
    <div class="person">
      <div class="person-name">Otto Velmar</div>
      <div class="person-role">Owner/Manager</div>
    </div>
    <div class="brand front-brand">Velmar's Bine Hollow</div>
    <div class="tagline front-tagline">Grower of High Quality Wisconsin Hops</div>
    <ul class="contacts">
      <li>
        <svg class="icon" viewBox="0 0 16 16"><circle cx="8" cy="8" r="8" fill="var(--white)"/><path d="M8 3.5a3 3 0 0 0-3 3c0 2.3 3 6 3 6s3-3.7 3-6a3 3 0 0 0-3-3z" fill="var(--maroon)"/></svg>
        1742 Millbrook Lane, Ashford, WI 53010
      </li>
      <li class="pair">
        <span class="item"><svg class="icon" viewBox="0 0 16 16"><circle cx="8" cy="8" r="8" fill="var(--white)"/><rect x="5.5" y="3.5" width="5" height="9" rx="1" fill="var(--maroon)"/></svg>608-555-0172</span>
        <span class="item"><svg class="icon" viewBox="0 0 16 16"><circle cx="8" cy="8" r="8" fill="var(--white)"/><path d="M5 4.5l2 0 .8 2-1.2 1a5 5 0 0 0 2 2l1-1.2 2 .8v2a1 1 0 0 1-1 1A7 7 0 0 1 4 5.5a1 1 0 0 1 1-1z" fill="var(--maroon)"/></svg>608-555-0139</span>
      </li>
      <li>
        <svg class="icon" viewBox="0 0 16 16"><circle cx="8" cy="8" r="7.2" fill="none" stroke="var(--white)" stroke-width="1.4"/><rect x="4" y="5.5" width="8" height="5.5" fill="none" stroke="var(--white)" stroke-width="1.1"/><path d="M4 5.5l4 3 4-3" fill="none" stroke="var(--white)" stroke-width="1.1"/></svg>
        binehollow@mailbox.net
      </li>
      <li>
        <svg class="icon" viewBox="0 0 16 16"><circle cx="8" cy="8" r="7" fill="none" stroke="var(--white)" stroke-width="1.4"/><ellipse cx="8" cy="8" rx="3" ry="7" fill="none" stroke="var(--white)" stroke-width="1.2"/><line x1="1" y1="8" x2="15" y2="8" stroke="var(--white)" stroke-width="1.2"/></svg>
        www.binehollow.com
      </li>
    </ul>
  </section>

</div>
</body>
</html>
```